Exclusive beauty salon needs a price list or services booklet

I need a new very attractive flyer for my beauty salon, containing information on the different services and their prices.
In attachment you can find a pdf of the "old" one, but I'd love to have a beautifully designed new one!
I'd love to have a booklet in format 148 x 148 mm, or in US format, containing 12 or 16 pages, but if you can offer other nice looking designs they are welcome!
The services that need to come in the booklet with their prices can all be found on my website: www.atelierv.be, starting with
Gelaatsverzorging
Wimperverlenging
Suikerontharing
Wimperlifting
Permanente Make Up
Airbrush Tanning

Target Market(s)

woman from 20 to 89 years old

Industry/Entity Type

Beauty Salon

Font styles to use
Sans Serif

Colors

Designer to choose colors to be used in the design.

Requirements
Must have
• a classy nice look, it must contain details about the services from my beauty salon and their prices, and nice pictures.
• The Names, prices and explanations of the services can easily be found on my website: www.atelierv.be
Nice to have
• In attachment you can find the "old" price list in pdf, what I need now is a "new booklet" with the new logo and updated services price list.
• I need a very nice and attractive looking booklet, classy chique, Paris chique, looking very expensive.
Should not have
• Not too much colors, not too curly, but still feminine

```html
<!DOCTYPE html>
<html lang="nl">
<head>
<meta charset="utf-8">
<title>Atelier V – Permanente Make Up</title>
<link href="https://fonts.googleapis.com/css2?family=Questrial&display=swap" rel="stylesheet">
<style>
  :root {
    --backdrop: #a9a9a9;
    --paper: #ffffff;
    --paper-shade: #efefef;
    --ink: #7d7d7d;
    --ink-soft: #8e8e8e;
    --rose: #d98f9a;
    --rose-dark: #d38692;
    --rose-light: #f0d3d7;
    --teal: #6fc3bb;
    --teal-light: #bfe5e1;
    --accent-line: #9cc7d2;
    --photo-dark: #3a3330;
    --photo-warm: #8a6a5e;
    --thumb-tone: #e8d9d3;
  }
  * { box-sizing: border-box; margin: 0; padding: 0; }
  html, body { width: 1200px; height: 523px; overflow: hidden; }
  body {
    background: var(--backdrop);
    font-family: "Questrial", sans-serif;
    color: var(--ink);
    position: relative;
  }
  .spread {
    position: absolute;
    left: 125px; top: 26px;
    width: 950px; height: 470px;
    display: flex;
  }
  .page {
    position: relative;
    width: 475px; height: 470px;
    background: var(--paper);
  }
  .page--left { background: linear-gradient(90deg, var(--paper) 85%, var(--paper-shade)); }
  .page--right { background: linear-gradient(90deg, var(--paper-shade), var(--paper) 12%); }

  .chapter-title {
    position: absolute; right: 24px; top: 15px;
    font-size: 15px; font-weight: 400; letter-spacing: 0.3px;
    color: var(--rose);
    text-transform: uppercase;
  }
  .hero-photo {
    position: absolute; left: 0; top: 50px;
    width: 475px; height: 212px;
    background: linear-gradient(180deg, var(--photo-warm), var(--photo-dark));
  }
  .consult {
    position: absolute; left: 92px; top: 312px; width: 315px;
  }
  .consult__title {
    font-size: 12.5px; font-weight: 400; text-transform: uppercase; color: var(--ink);
    border-left: 1.5px solid var(--accent-line);
    padding: 4px 0 4px 14px; margin-bottom: 10px;
  }
  .consult__text { font-size: 12.6px; line-height: 1.45; color: var(--ink-soft); padding-left: 15px; }

  .service { position: absolute; left: 0; width: 475px; }
  .service__bar {
    margin-left: 38px; height: 18px;
    display: flex; justify-content: space-between; align-items: center;
    padding: 0 30px 0 12px;
    color: var(--paper); font-size: 12px; text-transform: uppercase; letter-spacing: 0.3px;
    background: linear-gradient(90deg, var(--rose-dark), var(--rose-light));
  }
  .service__bar--teal { background: linear-gradient(90deg, var(--teal), var(--teal-light)); }
  .service__price { font-size: 10.5px; }
  .service__body {
    margin: 7px 0 0 28px; width: 300px;
    font-size: 8.4px; line-height: 1.55; color: var(--ink-soft);
  }
  .service__body p + p { margin-top: 8px; }
  .service__body ul { list-style: none; padding-left: 6px; }
  .service__thumb {
    position: absolute; right: 30px;
    width: 76px; height: 76px; border-radius: 50%;
    background: var(--thumb-tone);
    box-shadow: 0 1px 4px rgba(0,0,0,0.22);
  }

  .brand {
    position: absolute; right: 22px; bottom: 20px;
    display: flex; align-items: center; gap: 6px;
    font-size: 9px; letter-spacing: 2px; text-transform: uppercase; color: var(--ink);
  }
  .brand__mark { width: 9px; height: 9px; border: 1px solid var(--ink); }
</style>
</head>
<body>
  <main class="spread">
    <section class="page page--left">
      <h1 class="chapter-title">Permanente make up</h1>
      <div class="hero-photo" role="img" aria-label="Portretfoto van een vrouw met gesloten ogen en permanente make-up"></div>
      <div class="consult">
        <h2 class="consult__title">Gratis adviesgesprek</h2>
        <p class="consult__text">Het is mogelijk om eerst op consult te komen om te bespreken wat je graag zou willen. De gewenste vorm van uw wenkbrauwen, lippen of eyeliner word samen uitgetekend, we zoeken dan samen de kleur uit die jou gezicht het beste ophaalt en het mooiste bij je past, zodat je een idee krijgt van het resultaat.</p>
      </div>
    </section>

    <section class="page page--right">
      <article class="service" style="top:18px">
        <div class="service__bar"><span>Full lips</span><span class="service__price">€595</span></div>
        <div class="service__body">
          <p>Een kleuraccent aan uw mond</p>
          <ul>
            <li>-Uw herkende liplijn preciseert uw natuurlijke mond</li>
            <li>-Een schaduweffect waarbij de liplijn uitschaduwt op de mond</li>
            <li>-Full lips vervolledigt de natuurlijke lipkleur</li>
            <li>-Camoufleert oneffenheden zoals pigmentvlekjes, hypopigmentatie</li>
            <li>-Vergroot boven en/ of onderlip</li>
            <li>-Full lips kleurt de mond volledig</li>
          </ul>
        </div>
        <div class="service__thumb" role="img" aria-label="Close-up foto van lippen met permanente lipkleur" style="top:38px"></div>
      </article>

      <article class="service" style="top:164px">
        <div class="service__bar service__bar--teal"><span>Permanente make up volledige oogcontour</span><span class="service__price">€360</span></div>
        <div class="service__body">
          <p>Je tekent al jarenlang een lijntje boven en onder uw oog?</p>
          <p>Een perfecte vorm is nodig want dit vervangt wel degelijk uw make-up! Ik ben altijd eerlijk en oprecht want uw mooie liner is mijn beste reclame! Ik geef heel graag advies over de mogelijkheden.</p>
          <p>Alles wordt uitvoerig besproken en uitgetekend zo ziet u al hoe uw eyeliner er zal uitzien en kan u zelf aangeven of u deze fijner of net iets dikker wenst.</p>
        </div>
        <div class="service__thumb" role="img" aria-label="Close-up foto van een oog met volledige oogcontour" style="top:30px"></div>
      </article>

      <article class="service" style="top:296px">
        <div class="service__bar"><span>Brede eyeliner boven het oog</span><span class="service__price">€235</span></div>
        <div class="service__body">
          <p>Je tekent al jarenlang een "dikker" lijntje ?</p>
          <p>Een perfecte vorm is nodig want dit vervangt wel degelijk uw make-up! Ik ben altijd eerlijk en oprecht want uw mooie liner is mijn beste reclame! Ik geef heel graag advies over de mogelijkheden.</p>
          <p>Alles wordt uitvoerig besproken en uitgetekend zo ziet u al hoe uw eyeliner er zal uitzien en kan u zelf aangeven of u deze fijner of net iets dikker wenst.</p>
        </div>
        <div class="service__thumb" role="img" aria-label="Close-up foto van een oog met brede eyeliner" style="top:28px"></div>
      </article>

      <div class="brand"><span class="brand__mark"></span><span>Atelier V</span></div>
    </section>
  </main>
</body>
</html>
```